Bully breed rescue website

I need a website for my bully breed rescue. We rescue bully breeds from up and down the east coast of the United States and train them as service dogs for people with limited mobility disabilities. I don't want a lot of white space. I want it to be modern and slick and colorful and still look professional. I want it to be different and have a lot of wow factor. I linked a copy of my logo.

Number of Pages Required

5+ page

Font styles to use
Sans Serif

Colors

Designer to choose colors to be used in the design.

Requirements
Must have
• Moving aspects. Blog and ecommerce.
• 1.) Home page
• 2.) Services- something modular
• 3.) About US
• 4.) Blog
• 5.) Application page
• 6.) Donation page
• 7.) Contact Us
Nice to have
• Large Slider of photos on home page
• vertical menu bar
Should not have
• Lots of white space. Dont want it to look like a template or any other site

```html
<!DOCTYPE html>
<html lang="en">
<head>
<meta charset="utf-8">
<title>Quillmar Haven</title>
<link href="https://fonts.googleapis.com/css2?family=Poppins:wght@400;500;600;700&family=Teko:wght@400;500&display=swap" rel="stylesheet">
<style>
:root{
  --red:#c8141b;
  --brown:#7a4a2a;
  --orange:#e8651a;
  --peach:#fcc98a;
  --cream:#f4f1ec;
  --beige:#e0d2c6;
  --sand:#e9ddd0;
  --yellow:#e8a93a;
  --teal:#25b6b4;
  --blue:#2fa9d8;
  --pink:#ef4a6a;
  --gold:#f3b445;
  --ink:#2b2b2b;
  --muted:#555;
  --footer:#242424;
  --footer-text:#dddddd;
  --white:#fff;
}
*{margin:0;padding:0;box-sizing:border-box}
html,body{width:1200px;height:3758px;overflow:hidden}
body{font-family:"Poppins",sans-serif;color:var(--ink);background:var(--cream);position:relative}
.abs{position:absolute}
p{font-size:11px;line-height:19px;color:var(--muted)}

/* Header */
.hero{left:0;top:0;width:1200px;height:600px;background:linear-gradient(120deg,#3a2a22 0%,#6b4a35 35%,#3d3128 60%,#1f1b18 100%)}
.brand{left:213px;top:8px;display:flex;align-items:center;gap:10px;z-index:5}
.brand-dot{width:58px;height:58px;border-radius:50%;background:var(--white);border:3px solid var(--red)}
.brand-name{font-size:16px;font-weight:700;color:var(--white);white-space:nowrap}
.nav{left:476px;top:50px;width:500px;height:38px;background:var(--brown);display:flex;justify-content:space-around;align-items:center;z-index:5}
.nav a{color:var(--white);font-size:11px;font-weight:600;text-decoration:none;text-transform:uppercase}
.donate-tab{left:877px;top:0;width:140px;height:50px;background:var(--red);color:var(--white);font-size:13px;font-weight:700;display:flex;align-items:center;justify-content:center;clip-path:polygon(12% 0,100% 0,88% 100%,0 100%);z-index:5}
.hero-title{left:595px;top:280px;width:420px;text-align:center;color:var(--white);font-family:"Teko",sans-serif;line-height:1;white-space:nowrap}
.hero-title small{display:block;font-size:38px}
.hero-title strong{display:block;font-size:60px;font-weight:500}
.arrow{width:38px;height:38px;border-radius:50%;background:var(--white);display:flex;align-items:center;justify-content:center}
.red-band{left:0;top:576px;width:1200px;height:100px;background:var(--red);clip-path:polygon(0 0,100% 25%,100% 75%,0 100%)}

/* About */
.about{left:208px;top:656px;width:782px;height:376px;display:flex;box-shadow:0 4px 14px rgba(0,0,0,.15)}
.about-text{width:313px;background:var(--peach);padding:26px 24px}
.about-text h2{font-size:20px;font-weight:700;line-height:22px;text-transform:uppercase;margin-bottom:14px}
.about-text p{color:#5a4630;margin-bottom:10px;font-size:10.5px;line-height:18px}
.btn{display:inline-block;background:var(--orange);color:var(--white);font-size:10px;font-weight:600;padding:9px 18px;text-transform:uppercase;white-space:nowrap}
.about-photo{flex:1;background:linear-gradient(160deg,#6f8a4a,#3f5a2a 60%,#8a5a32)}
.mv{top:1065px;width:370px}
.mv h3{font-size:14px;font-weight:700;margin-bottom:8px;text-transform:uppercase}

/* Help */
.help{left:0;top:1215px;width:1200px;height:333px;background:var(--beige)}
.sec-title{width:1200px;left:0;text-align:center;font-size:19px;font-weight:700;text-transform:uppercase}
.card{top:1320px;width:248px;height:190px;color:var(--white);text-align:center;padding-top:22px}
.card .ic{width:52px;height:52px;border-radius:50%;border:2px solid var(--white);margin:0 auto 14px;display:flex;align-items:center;justify-content:center}
.card h4{font-size:15px;font-weight:600;text-transform:uppercase;margin-bottom:10px}
.card p{color:var(--white);font-size:10px;line-height:15px;padding:0 26px}

/* Sponsor */
.sponsor{left:0;top:1548px;width:1200px;height:180px;background:var(--yellow)}
.sponsor-text{left:235px;top:1604px;width:335px;text-align:center;color:var(--white);font-size:14px;line-height:21px}
.sponsor-photo{left:600px;top:1548px;width:390px;height:155px;background:linear-gradient(90deg,#d9a64a,#8f7a3a 50%,#c49a4f);clip-path:polygon(6% 0,100% 0,94% 100%,0 100%);border:4px solid var(--white)}

/* Dogs */
.dogs{left:0;top:1728px;width:1200px;height:402px;background:var(--brown)}
.dog{top:1898px;width:180px;height:181px;border:3px solid var(--white)}

/* Policies */
.policies{left:0;top:2130px;width:1200px;height:350px;background:linear-gradient(90deg,#4b3a22 0%,#5e4a2a 30%,#6c5a30 65%,#7a6a3a 100%)}
.policy-photo{left:0;top:2130px;width:240px;height:350px;background:linear-gradient(180deg,#6a4a2c,#8a5c34 55%,#4a5a2a)}
.pol-col{top:2285px;width:245px;text-align:center}
.pol-col h4{color:var(--white);font-size:14px;font-weight:500;margin-bottom:12px}
.pol-col p{color:#e8e2d6;font-size:10.5px;line-height:17px}

/* Rescue */
.rescue{left:0;top:2480px;width:1200px;height:446px;background:var(--brown)}
.rescue-photo{left:626px;top:2480px;width:574px;height:446px;background:linear-gradient(135deg,#3d4a2a,#6a6a3a 45%,#a07a4a)}
.rescue-text{left:208px;top:2530px;width:310px}
.rescue-text h3{color:var(--white);font-size:17px;font-weight:700;text-transform:uppercase;margin-bottom:14px}
.rescue-text p{color:#ecdfd2;font-size:10.5px;line-height:17px;margin-bottom:14px}
.rescue-text a{color:var(--gold);text-decoration:none}
.rbox{left:544px;width:446px;height:103px;display:flex;align-items:flex-start}
.rbox .side{width:70px;height:100%;display:flex;align-items:center;justify-content:center;background:rgba(255,255,255,.15)}
.rbox .body{padding:14px 18px;color:var(--white)}
.rbox h5{font-size:14px;font-weight:500;margin-bottom:6px}
.rbox p{color:var(--white);font-size:10.5px;line-height:16px}

/* Posts */
.posts{left:0;top:2926px;width:1200px;height:551px;background:var(--sand)}
.post{top:3031px;width:235px;height:339px;background:var(--white);box-shadow:0 2px 8px rgba(0,0,0,.12)}
.post .ph{height:133px;margin:6px}
.post .in{padding:10px 16px}
.post time{font-size:9px;color:#888}
.post h4{font-size:15px;font-weight:500;line-height:20px;margin:4px 0 10px}
.post p{font-size:10px;line-height:15px}
.post .more{font-size:9px;color:var(--orange);text-transform:uppercase;margin-top:12px;display:block}

/* Footer */
.footer{left:0;top:3477px;width:1200px;height:281px;background:var(--footer)}
.fnav{top:3505px;left:0;width:1200px;display:flex;justify-content:center;gap:26px}
.fnav a{color:var(--footer-text);font-size:11px;text-decoration:none}
.fcol{top:3565px;font-size:11px;line-height:20px;color:var(--footer-text)}
.fcol h6{font-size:11px;font-weight:600;color:var(--white);margin-bottom:6px}
.fbrand{left:470px;top:3560px;width:260px;text-align:center}
.fbrand .dot{width:56px;height:56px;border-radius:50%;border:2px solid var(--footer-text);margin:0 auto 8px}
.fbrand span{font-size:20px;font-weight:700;color:var(--white);white-space:nowrap}
.news{left:752px;top:3565px;width:238px}
.news h6{font-size:11px;font-weight:600;color:var(--white);margin-bottom:10px}
.news .row{display:flex}
.news .field{flex:1;height:32px;background:var(--white);font-size:10px;color:#999;padding:9px 10px}
.news .go{width:78px;height:32px;background:var(--orange);color:var(--white);font-size:10px;font-weight:600;display:flex;align-items:center;justify-content:center;text-transform:uppercase}
.social{display:flex;gap:8px;margin-top:14px}
.social i{width:12px;height:12px;border-radius:50%;background:var(--footer-text);display:block}
.copy{top:3722px;left:0;width:1200px;text-align:center;font-size:10px;color:#aaa}
</style>
</head>
<body>

<!-- Header / hero slider -->
<div class="abs hero" role="img" aria-label="Slider photo: bearded man in a shearling jacket hugging a brown and white pit bull outdoors"></div>
<div class="abs brand"><div class="brand-dot"></div><div class="brand-name">Quillmar Haven</div></div>
<div class="abs donate-tab">DONATE</div>
<nav class="abs nav"><a>Home</a><a>Services</a><a>About Us</a><a>Blog</a><a>Application</a><a>Donation</a><a>Contact Us</a></nav>
<div class="abs hero-title"><small>Welcome to</small><strong>Quillmar Haven</strong></div>
<div class="abs arrow" style="left:152px;top:318px"><svg width="14" height="14" viewBox="0 0 14 14"><path d="M9 2 4 7l5 5" stroke="#222" stroke-width="2" fill="none"/></svg></div>
<div class="abs arrow" style="left:1002px;top:318px"><svg width="14" height="14" viewBox="0 0 14 14"><path d="M5 2l5 5-5 5" stroke="#222" stroke-width="2" fill="none"/></svg></div>
<div class="abs red-band"></div>

<!-- About -->
<section class="abs about">
  <div class="about-text">
    <h2>About<br>Quillmar Haven</h2>
    <p>Lorem ipsum dolor sit amet, consectetur adipiscing elit, sed do eiusmod tempor incididunt ut labore et dolore magna aliqua. Ut enim ad minim veniam, quis nostrud exercitation ullamco laboris nisi ut aliquip ex ea commodo consequat. Duis aute irure dolor in reprehenderit in voluptate velit esse cillum dolore eu fugiat nulla pariatur.</p>
    <p>Excepteur sint occaecat cupidatat non proident, sunt in culpa qui officia deserunt mollit anim id est laborum.</p>
    <span class="btn">Read More</span>
  </div>
  <div class="about-photo" role="img" aria-label="Photo of a brown and white pit bull sitting on grass among autumn leaves"></div>
</section>
<div class="abs mv" style="left:208px"><h3>Our Mission</h3><p>Lorem ipsum dolor sit amet, consectetur adipiscing elit, sed do eiusmod tempor incididunt ut labore et dolore magna aliqua. Ut enim ad minim veniam, quis nostrud exercitation ullamco laboris nisi ut aliquip ex ea commodo consequat.</p></div>
<div class="abs mv" style="left:608px"><h3>Our Vision</h3><p>Lorem ipsum dolor sit amet, consectetur adipiscing elit, sed do eiusmod tempor incididunt ut labore et dolore magna aliqua. Ut enim ad minim veniam, quis nostrud exercitation ullamco laboris nisi ut aliquip ex ea commodo consequat.</p></div>

<!-- How you can help -->
<section class="abs help"></section>
<h2 class="abs sec-title" style="top:1265px">How You Can Help</h2>
<div class="abs card" style="left:208px;background:var(--blue)">
  <div class="ic"><svg width="24" height="24" viewBox="0 0 24 24"><path d="M12 21s-8-5-8-11a4.5 4.5 0 0 1 8-2.8A4.5 4.5 0 0 1 20 10c0 6-8 11-8 11z" fill="none" stroke="#fff" stroke-width="2"/></svg></div>
  <h4>Donate</h4><p>Sed ut perspiciatis unde omnis iste natus error sit voluptatem accusantium</p>
</div>
<div class="abs card" style="left:476px;background:var(--pink)">
  <div class="ic"><svg width="24" height="24" viewBox="0 0 24 24"><path d="M12 4v16M4 12h16" stroke="#fff" stroke-width="2.5"/></svg></div>
  <h4>Sponsor A Dog</h4><p>Sed ut perspiciatis unde omnis iste natus error sit voluptatem accusantium</p>
</div>
<div class="abs card" style="left:744px;background:var(--teal)">
  <div class="ic"><svg width="24" height="24" viewBox="0 0 24 24"><circle cx="12" cy="12" r="8" fill="none" stroke="#fff" stroke-width="2"/><path d="M12 7v5l3 3" stroke="#fff" stroke-width="2" fill="none"/></svg></div>
  <h4>Dire Cases</h4><p>Sed ut perspiciatis unde omnis iste natus error sit voluptatem accusantium</p>
</div>

<!-- Sponsor band -->
<section class="abs sponsor"></section>
<div class="abs sponsor-text">If you are interested in becoming a sponsor for Quillmar Haven please email at:<br><svg width="16" height="12" viewBox="0 0 16 12" style="vertical-align:middle;margin-right:6px"><rect x="1" y="1" width="14" height="10" fill="none" stroke="#fff" stroke-width="1.5"/><path d="M1 1l7 6 7-6" stroke="#fff" stroke-width="1.5" fill="none"/></svg>hello@quillmar-haven.example</div>
<div class="abs sponsor-photo" role="img" aria-label="Photo of two bully breed dogs running across a sunlit field"></div>

<!-- Dogs available -->
<section class="abs dogs"></section>
<h2 class="abs sec-title" style="top:1795px;color:#fff;font-size:18px">Dogs Available For Foster And/Or Adoption</h2>
<p class="abs" style="top:1832px;left:0;width:1200px;text-align:center;color:#f0e4d8;font-size:10.5px;line-height:16px">In a perfect world, every dog would have a home and every home would have a dog.<br>(Click on photo for more information)</p>
<svg class="abs" style="left:160px;top:1975px" width="30" height="26" viewBox="0 0 30 26"><path d="M28 13H4M12 4 3 13l9 9" stroke="#fff" stroke-width="3" fill="none"/></svg>
<div class="abs dog" style="left:208px;background:linear-gradient(135deg,#c9925e,#8a5a3a)" role="img" aria-label="Photo of a tan pit bull puppy"></div>
<div class="abs dog" style="left:408px;background:linear-gradient(135deg,#4a4a4a,#bdb6ae)" role="img" aria-label="Photo of a black and white pit bull"></div>
<div class="abs dog" style="left:609px;background:linear-gradient(135deg,#6a9a3a,#dcdcd4)" role="img" aria-label="Photo of a white pit bull lying on grass"></div>
<div class="abs dog" style="left:809px;background:linear-gradient(135deg,#3a3a3a,#6a7a4a)" role="img" aria-label="Photo of a black and white pit bull in a garden"></div>
<svg class="abs" style="left:1005px;top:1975px" width="30" height="26" viewBox="0 0 30 26"><path d="M2 13h24M18 4l9 9-9 9" stroke="#fff" stroke-width="3" fill="none"/></svg>

<!-- Policies -->
<section class="abs policies"></section>
<div class="abs policy-photo" role="img" aria-label="Photo of a brown pit bull lying in autumn leaves"></div>
<h2 class="abs sec-title" style="top:2178px;color:#fff;font-size:18px">Bully Breed Rescue Policies</h2>
<div class="abs" style="left:470px;top:2219px;width:260px;height:31px;background:var(--orange);color:#fff;font-size:9px;font-weight:600;display:flex;align-items:center;justify-content:center;text-transform:uppercase">Foster &amp; Adoption Policy - Please Read First</div>
<div class="abs pol-col" style="left:210px"><h4>Bully Breed Ambassadors</h4><p>Lorem ipsum dolor sit amet, consectetur adipiscing elit, sed do eiusmod tempor incididunt ut labore et dolore magna aliqua. Ut enim ad minim veniam, quis nostrud exercitation ullamco laboris nisi ut aliquip ex ea commodo consequat.</p></div>
<div class="abs pol-col" style="left:478px"><h4>For Accepting Shelter Dogs</h4><p>Lorem ipsum dolor sit amet, consectetur adipiscing elit, sed do eiusmod tempor incididunt ut labore et dolore magna aliqua. Ut enim ad minim veniam, quis nostrud exercitation ullamco laboris nisi ut aliquip ex ea commodo consequat.</p></div>
<div class="abs pol-col" style="left:746px"><h4>Owner Surrender &amp; Strays</h4><p>Lorem ipsum dolor sit amet, consectetur adipiscing elit, sed do eiusmod tempor incididunt ut labore et dolore magna aliqua. Ut enim ad minim veniam, quis nostrud exercitation ullamco laboris nisi ut aliquip ex ea commodo consequat.</p></div>

<!-- Rescue info -->
<section class="abs rescue"></section>
<div class="abs rescue-photo" role="img" aria-label="Photo of a smiling man playing with a pit bull outdoors"></div>
<div class="abs rescue-text">
  <h3>Bully Breed Rescue....</h3>
  <p>Sed ut perspiciatis unde omnis iste natus error sit voluptatem accusantium doloremque laudantium, totam rem aperiam, eaque ipsa quae ab illo inventore veritatis et quasi architecto beatae vitae dicta sunt explicabo. Nemo enim ipsam voluptatem quia voluptas sit aspernatur aut odit aut fugit, sed quia consequuntur magni dolores eos qui ratione voluptatem sequi nesciunt. Neque porro quisquam est, qui dolorem ipsum quia dolor sit amet, consectetur, adipisci velit, sed quia non numquam eius modi tempora incidunt ut labore et dolore magnam aliquam quaerat voluptatem. Ut enim ad minima veniam.</p>
  <p>If you have a rescue inquiry please email <a>rescue@quillmar-haven.example</a>. Your email will be forwarded to the appropriate volunteer.</p>
</div>
<div class="abs rbox" style="top:2535px;background:var(--teal)">
  <div class="side"><svg width="30" height="30" viewBox="0 0 30 30"><circle cx="11" cy="10" r="4" fill="none" stroke="#fff" stroke-width="2"/><circle cx="20" cy="12" r="3" fill="none" stroke="#fff" stroke-width="2"/><path d="M3 24c1-5 4-7 8-7s7 2 8 7M17 20c1-3 3-4 4-4 3 0 5 2 6 6" fill="none" stroke="#fff" stroke-width="2"/></svg></div>
  <div class="body"><h5>... is a volunteer only organization:</h5><p>Lorem ipsum dolor sit amet, consectetur adipiscing elit, sed do eiusmod tempor incididunt ut labore et dolore magna aliqua</p></div>
</div>
<div class="abs rbox" style="top:2644px;background:var(--gold)">
  <div class="side"><svg width="28" height="28" viewBox="0 0 28 28"><path d="M6 14l6 6 10-12" stroke="#fff" stroke-width="3" fill="none"/></svg></div>
  <div class="body"><h5>... accepts bully breed dogs that have:</h5><p>Lorem ipsum dolor sit amet, consectetur adipiscing elit, sed do eiusmod tempor incididunt ut labore et dolore magna aliqua</p></div>
</div>
<div class="abs rbox" style="top:2753px;background:var(--pink)">
  <div class="side"><svg width="28" height="28" viewBox="0 0 28 28"><path d="M14 24s-9-5-9-12a5 5 0 0 1 9-3 5 5 0 0 1 9 3c0 7-9 12-9 12z" fill="none" stroke="#fff" stroke-width="2"/></svg></div>
  <div class="body"><h5>... owner surrender &amp; strays:</h5><p>Lorem ipsum dolor sit amet, consectetur adipiscing elit, sed do eiusmod tempor incididunt ut labore et dolore magna aliqua</p></div>
</div>

<!-- Recent posts -->
<section class="abs posts"></section>
<h2 class="abs sec-title" style="top:2978px;font-size:18px">Recent Posts</h2>
<article class="abs post" style="left:208px"><div class="ph" style="background:linear-gradient(135deg,#c47a3a,#5a7a3a)" role="img" aria-label="Photo of a tan pit bull among flowers"></div><div class="in"><time>April 23, 2018</time><h4>Lorem ipsum dolor sit amet, consectetur</h4><p>Sed ut perspiciatis unde omnis iste natus error sit voluptatem accusantium totam rem aperiam</p><span class="more">Read More</span></div></article>
<article class="abs post" style="left:483px"><div class="ph" style="background:linear-gradient(135deg,#7aa04a,#e0ddd6)" role="img" aria-label="Photo of a white pit bull on grass"></div><div class="in"><time>April 23, 2018</time><h4>Lorem ipsum dolor sit amet, consectetur</h4><p>Sed ut perspiciatis unde omnis iste natus error sit voluptatem accusantium totam rem aperiam</p><span class="more">Read More</span></div></article>
<article class="abs post" style="left:752px"><div class="ph" style="background:linear-gradient(135deg,#5a7a3a,#a0623a)" role="img" aria-label="Photo of a red pit bull standing on a park path"></div><div class="in"><time>April 23, 2018</time><h4>Lorem ipsum dolor sit amet, consectetur</h4><p>Sed ut perspiciatis unde omnis iste natus error sit voluptatem accusantium totam rem aperiam</p><span class="more">Read More</span></div></article>
<div class="abs btn" style="left:540px;top:3387px;width:120px;text-align:center;padding:9px 0">Read More Blog</div>

<!-- Footer -->
<footer class="abs footer"></footer>
<nav class="abs fnav"><a>Home</a><a>Services</a><a>About US</a><a>Blog</a><a>Application</a><a>Donation</a><a>Contact Us</a></nav>
<div class="abs fcol" style="left:183px"><h6>Address</h6>Quillmar Haven<br>Lorem ipsum dolor<br>Adipiscing elit DO455</div>
<div class="abs fcol" style="left:325px"><h6>Call Us</h6><span style="font-size:19px;color:#fff">555-014-2290</span></div>
<div class="abs fbrand"><div class="dot"></div><span>Quillmar Haven</span></div>
<div class="abs news"><h6>Sign Up To Our Newsletter</h6><div class="row"><div class="field">Your email address</div><div class="go">Sign Up</div></div><div class="social"><i></i><i></i><i></i></div></div>
<div class="abs copy">©2018 Quillmar Haven. All Rights Reserved. &nbsp; Privacy Policy</div>

</body>
</html>
```